Larkin Ridge Provisions Co Website Creation

We need a website designed that goes along with our western/cattle brand vibe that our logo has. We are going to need a couple different pages including: About Us, Meat Boxes, Recipes, Contact Us.

We are going to need a shop so that people may visit the website and order meat boxes to be shipped or delivered at their home. Our mission is to provide the highest quality meat that every family can afford.

Would love to see the website design with lots of mountain range backgrounds and create a feel of open range beef that has a tradition of providing great beef. Family owned business that has been raising cattle for over 30 years.

Love the colors of using dark greens, browns, Tans, Blacks

```html
<!DOCTYPE html>
<html lang="en">
<head>
<meta charset="utf-8">
<title>Larkin Ridge Provisions Co</title>
<link href="https://fonts.googleapis.com/css2?family=Bebas+Neue&family=Poppins:wght@400;500;600&display=swap" rel="stylesheet">
<style>
:root{
  --green:#0a3d08;
  --green-dark:#072e06;
  --brown:#3a1a0e;
  --maroon:#6e2a25;
  --ink:#1d1d1d;
  --grey:#7a7a7a;
  --footer:#2d2c2c;
  --white:#ffffff;
  --line:#e4e4e4;
}
*{margin:0;padding:0;box-sizing:border-box}
html,body{width:1200px;height:3923px;overflow:hidden}
body{position:relative;background:var(--white);font-family:'Poppins',sans-serif;color:var(--ink)}
.abs{position:absolute}
.display{font-family:'Bebas Neue',sans-serif;font-weight:400;letter-spacing:.5px}
a{text-decoration:none;color:inherit}

/* header */
.site-header{position:absolute;left:0;top:0;width:1200px;height:69px;background:var(--white);z-index:5}
.main-nav{position:absolute;left:88px;top:27px;display:flex;gap:16px;font-size:10.5px;font-weight:500;color:var(--green)}
.main-nav .active{position:relative}
.main-nav .active::after{content:"";position:absolute;left:0;right:0;top:38px;height:3px;background:var(--brown)}
.brand-tab{position:absolute;left:540px;top:0;width:120px;height:110px;z-index:6}
.brand-tab svg{position:absolute;left:0;top:0}
.brand-name{position:absolute;left:0;top:16px;width:120px;text-align:center;font-family:'Bebas Neue',sans-serif;font-size:19px;line-height:19px;color:var(--green)}
.header-icon{position:absolute;top:22px}
.search{position:absolute;left:926px;top:15px;width:184px;height:38px;display:flex}
.search span{flex:1;background:#ececec;font-size:11px;line-height:38px;padding-left:18px;color:#333}
.search b{width:44px;background:var(--brown);display:flex;align-items:center;justify-content:center}

/* hero */
.hero{position:absolute;left:0;top:69px;width:1200px;height:592px;background:linear-gradient(100deg,#141414 0%,#2a2622 45%,#3a2d2a 62%,#1b1d24 100%)}
.hero-photo{position:absolute;left:500px;top:140px;width:440px;height:330px;border-radius:40% 30% 20% 30%;background:radial-gradient(ellipse at 50% 50%,#b83a3a 0%,#8e2426 45%,rgba(60,30,30,0) 72%)}
.hero-title{position:absolute;left:87px;top:230px;font-size:58px;line-height:65px;color:var(--white)}
.hero-sub{position:absolute;left:88px;top:364px;font-size:13.5px;font-weight:600;color:var(--white)}
.hero-text{position:absolute;left:88px;top:392px;width:400px;font-size:12.5px;line-height:20px;color:var(--white)}
.btn{position:absolute;display:flex;align-items:center;justify-content:center;font-size:13px;font-weight:600}
.btn-solid{background:var(--green);color:var(--white)}
.btn-ghost{border:2px solid var(--white);color:var(--white)}
.btn-outline{border:1.5px solid var(--green);color:var(--green);background:var(--white)}
.slider-arrow{position:absolute;width:40px;height:40px;border-radius:50%;display:flex;align-items:center;justify-content:center}

/* about */
.about-photo{position:absolute;left:157px;top:624px;width:396px;height:413px;background:linear-gradient(160deg,#1f1c22 0%,#3b2a2a 45%,#8c3a33 70%,#6b4a25 100%)}
.play{position:absolute;left:146px;top:133px}
.about-card{position:absolute;left:553px;top:624px;width:490px;height:413px;background:var(--white);box-shadow:0 6px 24px rgba(0,0,0,.07)}
.section-title{color:var(--green);font-size:40px;line-height:40px}
.body-copy{font-size:12px;line-height:19.5px;color:var(--grey)}
.ticks{position:absolute;left:84px;top:260px;display:flex;gap:16px;font-family:'Bebas Neue',sans-serif;font-size:13px;color:var(--ink);align-items:center}
.ticks span{display:flex;align-items:center;gap:6px}

/* why choose */
.feature{position:absolute;top:1202px;width:324px;height:240px;background:var(--white);box-shadow:0 4px 20px rgba(0,0,0,.08);text-align:center}
.feature.highlight{background:var(--green)}
.feature svg{position:absolute;left:127px;top:20px}
.feature h3{position:absolute;left:0;top:118px;width:100%;font-family:'Bebas Neue',sans-serif;font-weight:400;font-size:18px;color:var(--green)}
.feature p{position:absolute;left:40px;top:148px;width:244px;font-size:12px;line-height:19.5px;color:var(--grey)}
.feature.highlight h3,.feature.highlight p{color:var(--white)}

/* banner */
.promo{position:absolute;left:0;top:1634px;width:1200px;height:350px;background:linear-gradient(90deg,#111 0%,#1e1e1e 40%,#3a2626 70%,#7d3434 100%)}
.promo-title{position:absolute;left:88px;top:124px;font-size:38px;color:var(--white)}
.promo-text{position:absolute;left:88px;top:172px;width:380px;font-size:12.5px;line-height:20px;color:var(--white)}
.text-link{font-size:12.5px;font-weight:600;padding-bottom:2px}

/* steps */
.step-photo{position:absolute;width:508px;height:323px}
.step-title{font-size:40px;color:var(--green)}

/* testimonials */
.quote-card{position:absolute;top:2886px;height:255px;text-align:center}
.quote-mark{font-family:Georgia,serif;font-size:90px;line-height:60px;font-weight:700}
.quote-text{font-size:15px;line-height:23px}
.quote-name{font-family:'Bebas Neue',sans-serif;font-size:20px;letter-spacing:1px}
.dots{position:absolute;left:551px;top:3189px;display:flex;gap:7px}
.dots i{display:block;width:19px;height:4px;background:#e3e3e3}
.dots i.on{background:var(--green)}

/* newsletter + footer */
.site-footer{position:absolute;left:0;top:3491px;width:1200px;height:432px;background:var(--footer)}
.signup{position:absolute;left:90px;top:3241px;width:1016px;height:324px;background:linear-gradient(90deg,#7a2a25 0%,#5c3a2a 25%,#4e3a2c 45%,#5a4534 100%)}
.signup h2{position:absolute;left:614px;top:92px;font-size:38px;color:var(--white)}
.signup p{position:absolute;left:614px;top:146px;width:345px;font-size:12.5px;line-height:20px;color:var(--white)}
.signup-form{position:absolute;left:614px;top:199px;width:280px;height:37px;display:flex}
.signup-form span{flex:1;background:#2a2a2a;color:var(--white);font-size:12px;font-weight:500;line-height:37px;padding-left:18px}
.signup-form b{width:55px;background:var(--white);display:flex;align-items:center;justify-content:center}
.footer-brand{position:absolute;left:140px;top:3660px;width:220px;text-align:center;font-family:'Bebas Neue',sans-serif;font-size:34px;line-height:36px;color:var(--white)}
.footer-col{position:absolute;top:3662px;color:var(--white)}
.footer-col h4{font-family:'Bebas Neue',sans-serif;font-weight:400;font-size:16px;margin-bottom:14px}
.footer-col li{list-style:none;font-size:11px;line-height:20px;color:#cfcfcf}
.contact-row{display:flex;gap:10px;font-size:11px;line-height:17px;color:#e6e6e6;margin-bottom:14px}
.social{display:flex;gap:7px}
.social i{display:block;width:28px;height:28px;border:1.5px solid var(--white);border-radius:50%}
.footer-rule{position:absolute;left:134px;top:3850px;width:928px;height:1px;background:#5a5a5a}
.legal{position:absolute;top:3880px;font-size:10px;color:var(--white)}
</style>
</head>
<body>

<header class="site-header">
  <nav class="main-nav">
    <a class="active">HOME</a><a>ABOUT US</a><a>MEAT BOXES</a><a>RECIPES</a><a>CONTACT US</a>
  </nav>
  <svg class="header-icon" style="left:820px" width="22" height="22" viewBox="0 0 22 22" fill="none" stroke="#3a1a0e" stroke-width="1.6"><circle cx="11" cy="7" r="5"/><path d="M2 21c1-5 5-7 9-7s8 2 9 7"/></svg>
  <svg class="header-icon" style="left:872px" width="24" height="22" viewBox="0 0 24 22" fill="none" stroke="#3a1a0e" stroke-width="1.6"><path d="M1 2h4l3 12h12l2-8H7"/><circle cx="9" cy="19" r="1.6"/><circle cx="18" cy="19" r="1.6"/></svg>
  <div class="search"><span>Search</span><b><svg width="13" height="13" viewBox="0 0 13 13" fill="none" stroke="#fff" stroke-width="1.6"><circle cx="5.5" cy="5.5" r="4.3"/><path d="M8.6 8.6L12 12"/></svg></b></div>
</header>

<div class="brand-tab">
  <svg width="120" height="110" viewBox="0 0 120 110"><path d="M0 0H120V70L60 110L0 70Z" fill="#fff"/></svg>
  <div class="brand-name">Larkin Ridge<br>Provisions Co</div>
</div>

<section class="hero" role="img" aria-label="Butcher with a knife behind a thick bone-in steak on dark slate">
  <div class="hero-photo"></div>
</section>
<h1 class="display hero-title abs">PREMIUM OPEN RANGE<br>BEEF DELIVERED TO</h1>
<p class="hero-sub">YOUR DOORSTEP – TRADITION, QUALITY, AND FAMILY PRIDE.</p>
<p class="hero-text">Experience the finest cuts of beef from cattle raised on our family-owned ranch for over 30 years.</p>
<a class="btn btn-solid" style="left:88px;top:446px;width:115px;height:44px">SHOP NOW</a>
<a class="btn btn-ghost" style="left:219px;top:446px;width:116px;height:44px">READ MORE</a>
<div class="slider-arrow" style="left:21px;top:325px;border:1.5px solid #fff"><svg width="8" height="10" viewBox="0 0 8 10" fill="none" stroke="#fff" stroke-width="1.6"><path d="M6 1L2 5l4 4"/></svg></div>
<div class="slider-arrow" style="left:1128px;top:325px;background:#fff"><svg width="8" height="10" viewBox="0 0 8 10" fill="none" stroke="#222" stroke-width="1.6"><path d="M2 1l4 4-4 4"/></svg></div>

<section>
  <div class="about-photo" role="img" aria-label="Cubes of raw beef tumbling onto a wooden cutting board">
    <svg class="play" width="104" height="104" viewBox="0 0 104 104"><circle cx="52" cy="52" r="50" fill="#0a3d08" stroke="#8c8c8c" stroke-width="4"/><path d="M42 35L72 52L42 69Z" fill="#fff"/></svg>
  </div>
  <div class="about-card">
    <h2 class="display section-title abs" style="left:84px;top:54px">ABOUT US</h2>
    <p class="body-copy abs" style="left:84px;top:106px;width:365px">we take pride in our family tradition of raising cattle the way it's meant to be – sustainably, naturally, and with a deep respect for the land. For over 30 years, our family has been dedicated to providing the highest quality beef to families across the country. Our open-range cattle are grass-fed and grain-finished, ensuring the rich flavor and tender texture that sets our meat apart.</p>
    <div class="ticks">
      <span><svg width="13" height="13" viewBox="0 0 13 13"><circle cx="6.5" cy="6.5" r="6.5" fill="#0a3d08"/><path d="M3.5 6.7l2 2 4-4" stroke="#fff" stroke-width="1.5" fill="none"/></svg>ORGANIC MEAT</span>
      <span><svg width="13" height="13" viewBox="0 0 13 13"><circle cx="6.5" cy="6.5" r="6.5" fill="#0a3d08"/><path d="M3.5 6.7l2 2 4-4" stroke="#fff" stroke-width="1.5" fill="none"/></svg>PAYMENT SECURATION</span>
    </div>
    <a class="btn btn-outline" style="left:84px;top:308px;width:116px;height:44px">READ MORE</a>
  </div>
</section>

<section>
  <h2 class="display section-title abs" style="left:0;top:1120px;width:1180px;text-align:center">WHY CHOOSE US</h2>
  <div class="feature" style="left:88px">
    <svg width="70" height="80" viewBox="0 0 70 80" fill="none" stroke="#0a3d08" stroke-width="1.8"><circle cx="35" cy="30" r="26"/><circle cx="35" cy="30" r="18"/><path d="M35 19l3.3 7 7.5.8-5.6 5 1.6 7.4L35 35.4l-6.8 3.8 1.6-7.4-5.6-5 7.5-.8Z"/><path d="M22 52l-6 24 9-5 5 8 5-18M48 52l6 24-9-5-5 8"/></svg>
    <h3>PREMIUM QUALITY BEEF</h3>
    <p>Our cattle are grass-fed and grain-finished, ensuring rich flavor and tenderness in every bite.</p>
  </div>
  <div class="feature highlight" style="left:436px">
    <svg width="70" height="80" viewBox="0 0 70 80" fill="none" stroke="#fff" stroke-width="1.8"><path d="M8 6l54 66M62 6L8 72"/><rect x="4" y="2" width="10" height="10"/><rect x="56" y="2" width="10" height="10"/><circle cx="35" cy="39" r="12"/><path d="M35 22v34M18 39h34"/></svg>
    <h3>FAMILY OWNED AND OPERATED</h3>
    <p>With over 30 years of ranching experience, we bring generations of expertise and care to every product we offer.</p>
  </div>
  <div class="feature" style="left:783px">
    <svg width="70" height="80" viewBox="0 0 70 80" fill="none" stroke="#0a3d08" stroke-width="1.8"><path d="M37 10v42M37 30c-4-10-12-12-18-10 2 8 10 12 18 10M37 22c4-10 12-12 18-10-2 8-10 12-18 10"/><path d="M4 56h12l14 6h14c4 0 4 6 0 6H30M16 74l10 4 28-8 12-10-6-4-18 8"/></svg>
    <h3>SUSTAINABLY RAISED</h3>
    <p>We prioritize sustainable farming practices, respecting the land and ensuring the health and well-being of our cattle.</p>
  </div>
  <a class="btn btn-solid" style="left:542px;top:1497px;width:114px;height:43px">READ MORE</a>
</section>

<section class="promo" role="img" aria-label="Raw steaks with chili peppers, peppercorns and rosemary on black slate">
  <h2 class="display promo-title">SAVOR FRESH: GRILL &amp; GIFT</h2>
  <p class="promo-text">We Source our meat and seafood from partners with the highest standards for quality.</p>
  <a class="text-link abs" style="left:88px;top:224px;color:#fff;border-bottom:1.5px solid #fff">LEARN MORE</a>
</section>

<section>
  <div class="step-photo" style="left:90px;top:2074px;background:linear-gradient(135deg,#3a2e28 0%,#6a5046 40%,#7c3434 60%,#2b2420 100%)" role="img" aria-label="Hands slicing a cut of beef with a knife on a stone board"></div>
  <h2 class="display step-title abs" style="left:685px;top:2166px">YOU CHOOSE</h2>
  <p class="body-copy abs" style="left:685px;top:2214px;width:315px">Choose from 3 curated boxes or create your own custom box. Select a delivery frequency that meets your needs.</p>
  <a class="text-link abs" style="left:685px;top:2285px;color:var(--maroon);border-bottom:1.5px solid var(--maroon)">VIEW BOX OPTIONS</a>

  <h2 class="display step-title abs" style="left:190px;top:2512px">WE DELIVER</h2>
  <p class="body-copy abs" style="left:190px;top:2560px;width:290px">Your order ships for free, frozen for freshness and packed in an eco-friendly box.</p>
  <a class="text-link abs" style="left:190px;top:2612px;color:var(--maroon);border-bottom:1.5px solid var(--maroon)">SEE MORE ABOUT OUR BOXES</a>
  <div class="step-photo" style="left:599px;top:2399px;background:linear-gradient(160deg,#2a2a2a 0%,#8a3030 45%,#a84444 60%,#5a3a24 100%)" role="img" aria-label="Raw beef cuts arranged on a wooden board beside a black gift box"></div>
</section>

<section>
  <h2 class="display section-title abs" style="left:0;top:2796px;width:1200px;text-align:center">TESTIMONIALS</h2>
  <div class="quote-card" style="left:148px;width:420px">
    <div class="quote-mark" style="color:var(--green);margin-top:42px">“</div>
    <p class="quote-text" style="color:var(--grey);margin-top:12px">“Hollow Creek Outfitters has significantly improved our waste management processes. Their services are efficient and reliable.”</p>
    <p class="quote-name" style="color:var(--green);margin-top:20px">- DANA WHITFIELD</p>
  </div>
  <div class="quote-card" style="left:567px;width:466px;background:var(--green)">
    <div class="quote-mark" style="color:var(--white);margin-top:42px">“</div>
    <p class="quote-text" style="color:var(--white);margin:12px 40px 0">“We appreciate their commitment to sustainability and the environment. Their recycling programs are top-notch.”</p>
    <p class="quote-name" style="color:var(--white);margin-top:20px">- OWEN CASTELL</p>
  </div>
  <div class="dots"><i class="on"></i><i></i><i></i><i></i></div>
</section>

<footer class="site-footer"></footer>

<section class="signup" role="img" aria-label="Raw steaks, peppercorns and a carving fork on a rustic wooden table">
  <h2 class="display">JOIN OUR LIST</h2>
  <p>Be the first to know about new products, special offers, and delicious Ranch Kitchen content!</p>
  <div class="signup-form"><span>Email Address</span><b><svg width="14" height="14" viewBox="0 0 14 14"><path d="M1 6.5L13 1 9 13 6.8 8.2Z" fill="#0a3d08"/></svg></b></div>
</section>

<div class="footer-brand">Larkin Ridge<br>Provisions Co</div>

<div class="footer-col" style="left:436px">
  <h4>QUICK LINKS</h4>
  <ul><li>Home</li><li>About Us</li><li>Meat Boxes</li><li>Recipes</li><li>Contact Us</li></ul>
</div>
<div class="footer-col" style="left:634px">
  <h4>CONTACT US</h4>
  <div class="contact-row"><svg width="11" height="11" viewBox="0 0 11 11" style="margin-top:3px"><rect x="0" y="1.5" width="11" height="8" fill="#fff"/><path d="M0 2l5.5 4L11 2" stroke="#2d2c2c" fill="none"/></svg><span style="text-decoration:underline">info@larkinridge.com</span></div>
  <div class="contact-row"><svg width="11" height="13" viewBox="0 0 11 13" style="margin-top:3px"><path d="M5.5 0a5 5 0 0 1 5 5c0 3.5-5 8-5 8s-5-4.5-5-8a5 5 0 0 1 5-5z" fill="#fff"/><circle cx="5.5" cy="5" r="1.8" fill="#2d2c2c"/></svg><span>412 Cedar Hollow Road,<br>Millbrook PA, 17920</span></div>
</div>
<div class="footer-col" style="left:894px">
  <h4>FOLLOW UP</h4>
  <div class="social"><i></i><i></i><i></i><i></i></div>
</div>

<div class="footer-rule"></div>
<p class="legal" style="left:131px">Copyright© 2024 - <span style="text-decoration:underline">Larkin Ridge Provisions Co</span></p>
<p class="legal" style="left:854px">Privacy Policy<span style="margin:0 24px">|</span>Terms &amp; Conditions</p>

</body>
</html>
```